***Dozing Heron Brow Parlour is in need of a web site makeover***

I need a makeover for my existing web site. www.dozing-heron.com

Please help!!!! Thanks 😁

Dozing Heron Brow Parlour is an eyelash extension salon. In addition, we also provide skincare services (facials, waxing, etc). Our web site needs to appear professional and intuitive. In addition, allowing for ease of online booking is of utmost importance.

The client web site experience:
- esthetically pleasing and makes sense
- clearly recognize brand (Dozing Heron)
- easy to follow web pages
- easy to book appointments online
- easy to sign up for email updates
- easily locate services menu and pricing

Target Market(s)

Dozing Heron Brow Parlour offers eyelash extension services, as well as various skincare services (I.e. facials, waxing, etc.)

Industry/Entity Type

Beauty Salon

Number of Pages Required

5+ page

Font styles to use
Sans Serif
Script

Colors
000000
fee3d5
eaeaea
ffffff

Requirements
Must have
• - Home page with static contact information
• - Services page (menu of services and pricing)
• - Photo gallery page
• - Contact page
• - Q&A page
Nice to have
• Professional, classy, intuitive and simple for clients to be able to book online.

```html
<!DOCTYPE html>
<html lang="en">
<head>
<meta charset="utf-8">
<title>Dozing Heron Brow Parlour</title>
<link href="https://fonts.googleapis.com/css2?family=Lobster&family=Open+Sans:wght@400;600;700&display=swap" rel="stylesheet">
<style>
:root{
  --black:#000000;
  --ink:#1a1a1a;
  --peach:#fee3d5;
  --peach-deep:#e9c3ad;
  --mist:#eaeaea;
  --white:#ffffff;
  --grey:#6b6b6b;
  --line:#cfcfcf;
}
*{margin:0;padding:0;box-sizing:border-box}
html,body{width:1200px;height:2860px;overflow:hidden}
body{position:relative;background:var(--white);font-family:"Open Sans",Arial,sans-serif;color:var(--ink)}
.script{font-family:"Lobster",cursive;font-weight:400}

/* header */
.site-header{position:absolute;left:0;top:0;width:1200px;height:110px;z-index:5}
.site-header svg{position:absolute;inset:0}
.brand{position:absolute;left:40px;top:22px;display:flex;align-items:center;gap:12px}
.brand-dot{width:44px;height:44px;border-radius:50%;background:var(--peach)}
.brand-name{color:var(--white);font-size:18px;font-weight:600;letter-spacing:.5px;line-height:1.15;width:150px}
.main-nav{position:absolute;right:50px;top:52px;display:flex;gap:30px}
.main-nav a{color:#bdbdbd;font-size:13px;font-weight:600;letter-spacing:1px;text-decoration:none;text-transform:uppercase}
.main-nav a.active{color:var(--white)}

/* hero */
.hero{position:absolute;left:0;top:0;width:1200px;height:640px;background:linear-gradient(90deg,#f4f4f4 0%,#e6e6e6 55%,#d8d8d8 100%)}
.hero-photo{position:absolute;right:40px;top:80px;width:560px;height:560px;background:radial-gradient(ellipse at 60% 45%,#cfcfcf 0%,#9a9a9a 45%,#e3e3e3 80%)}
.hero-copy{position:absolute;left:140px;top:270px;width:500px}
.hero-copy h1{font-size:50px;color:var(--ink);margin-bottom:18px}
.hero-copy p{font-size:14px;line-height:1.7;color:var(--grey);margin-bottom:34px}
.btn{display:inline-block;background:linear-gradient(180deg,var(--peach),var(--peach-deep));color:var(--ink);font-size:14px;font-weight:700;letter-spacing:1px;padding:14px 30px;text-transform:uppercase;border:1px solid #d9b39c}
.slider-dots{position:absolute;left:570px;top:606px;display:flex;gap:8px}
.slider-dots span{width:9px;height:9px;border-radius:50%;background:#9a9a9a}
.slider-dots span.on{background:var(--ink)}

/* welcome */
.welcome{position:absolute;left:0;top:640px;width:1200px;height:340px;background:var(--mist)}
.welcome-photo{position:absolute;left:0;top:0;width:600px;height:340px;background:linear-gradient(135deg,#8c8c8c 0%,#2c2c2c 45%,#111 70%,#5c5c5c 100%)}
.welcome-card{position:absolute;left:580px;top:68px;width:580px;height:310px;background:var(--white);padding:40px 40px;box-shadow:0 4px 18px rgba(0,0,0,.18);z-index:3}
.welcome-card h2{font-size:32px;margin-bottom:18px}
.welcome-card p{font-size:14px;line-height:1.75;color:var(--grey)}

/* appointment */
.appointment{position:absolute;left:0;top:980px;width:1200px;height:510px;background:linear-gradient(90deg,#5a5a5a 0%,#2b2b2b 40%,#1a1a1a 100%)}
.appointment-photo{position:absolute;right:0;top:20px;width:540px;height:490px;background:radial-gradient(ellipse at 45% 40%,#bdbdbd 0%,#6d6d6d 40%,#222 85%)}
.appointment-card{position:absolute;left:40px;top:130px;width:580px;height:330px;background:var(--black);padding:44px 40px}
.appointment-card h2{color:var(--white);font-size:34px;margin-bottom:18px}
.appointment-card p{color:#bdbdbd;font-size:14px;line-height:1.75;margin-bottom:30px}

/* services */
.services{position:absolute;left:0;top:1490px;width:1200px;height:380px}
.section-title{text-align:center;font-size:36px;color:var(--ink)}
.services .section-title{margin-top:28px}
.section-intro{width:900px;margin:16px auto 0;text-align:center;font-size:13px;line-height:1.7;color:var(--grey)}
.service-grid{position:absolute;left:112px;top:150px;display:flex;gap:32px}
.service-card{position:relative;width:304px;height:200px}
.service-card .photo{position:absolute;inset:0;background:linear-gradient(160deg,#e0e0e0 0%,#9c9c9c 50%,#d4d4d4 100%)}
.service-card .label{position:absolute;left:0;bottom:0;width:100%;height:42px;background:var(--black);color:var(--white);font-size:15px;font-weight:600;display:flex;align-items:center;justify-content:center}

/* prices */
.prices{position:absolute;left:0;top:1870px;width:1200px;height:380px}
.prices .section-title{margin-top:20px}
.prices .section-intro{margin-top:8px}
.price-grid{position:absolute;left:112px;top:120px;width:976px;display:grid;grid-template-columns:472px 472px;column-gap:32px;row-gap:30px}
.price-item .head{display:flex;justify-content:space-between;font-size:15px;font-weight:700;padding-bottom:8px;border-bottom:1px solid var(--line);margin-bottom:10px}
.price-item p{font-size:12.5px;line-height:1.7;color:var(--grey)}

/* gallery */
.gallery{position:absolute;left:0;top:2250px;width:1200px;height:300px}
.gallery svg.band{position:absolute;inset:0}
.gallery .section-title{position:relative;color:var(--white);padding-top:52px}
.gallery-row{position:absolute;left:120px;top:125px;display:flex;gap:30px}
.gallery-row .photo{width:222px;height:140px;background:linear-gradient(150deg,#dcdcdc 0%,#8a8a8a 55%,#c9c9c9 100%)}
.gallery .arrow{position:absolute;top:178px}
.gallery .arrow.prev{left:70px}
.gallery .arrow.next{right:70px}

/* footer */
.site-footer{position:absolute;left:0;top:2550px;width:1200px;height:310px}
.footer-col{position:absolute;top:42px}
.footer-col h3{font-size:13px;font-weight:700;letter-spacing:1px;text-transform:uppercase;margin-bottom:14px}
.footer-col a{display:block;font-size:12.5px;color:var(--grey);text-decoration:none;line-height:26px}
.col-info{left:112px}
.col-links{left:300px}
.col-more{left:490px}
.contact-box{position:absolute;left:680px;top:30px;width:420px;height:200px;border:1px solid var(--line);padding:26px 34px}
.contact-row{display:flex;align-items:center;gap:16px;font-size:20px;font-weight:600}
.contact-row.email{font-size:16px;font-weight:400;margin-top:18px}
.icon-circle{width:40px;height:40px;border-radius:50%;background:var(--black);display:flex;align-items:center;justify-content:center;flex:none}
.social{display:flex;gap:14px;margin:18px 0 0 56px}
.social span{width:30px;height:30px;border-radius:50%;background:var(--ink)}
.copyright{position:absolute;left:112px;top:272px;font-size:11.5px;color:var(--grey)}
</style>
</head>
<body>

<div class="hero">
  <div class="hero-photo" role="img" aria-label="Portrait of a woman with smooth glowing skin, soft black and white studio light"></div>
  <div class="hero-copy">
    <h1 class="script">Skincare Services</h1>
    <p>Gentle, tailored treatments that refresh your skin and bring out your natural glow. Every visit begins with a calm consultation so your routine suits you.</p>
    <a class="btn">Book Now</a>
  </div>
  <div class="slider-dots"><span></span><span class="on"></span><span></span><span></span></div>
</div>

<header class="site-header">
  <svg width="1200" height="110" viewBox="0 0 1200 110" aria-hidden="true">
    <path d="M0 0H1200V80Q600 40 0 100Z" fill="#000000"/>
  </svg>
  <div class="brand">
    <span class="brand-dot"></span>
    <span class="brand-name">Dozing Heron Brow Parlour</span>
  </div>
  <nav class="main-nav">
    <a class="active">Home</a><a>Services</a><a>Pricing</a><a>Gallery</a><a>Sign Up</a><a>Appointment Booking</a><a>Contact Us</a>
  </nav>
</header>

<section class="welcome">
  <div class="welcome-photo" role="img" aria-label="Back view of a woman with long sleek dark hair"></div>
  <div class="welcome-card">
    <h2 class="script">Welcome To Dozing Heron</h2>
    <p>Dozing Heron Brow Parlour is a calm studio for lash extensions, brows and skincare. Our trained artists take time to learn what you love, then shape every set with care. We use gentle products, clean tools and a relaxed pace, so each appointment feels like a small escape from a busy day.</p>
  </div>
</section>

<section class="appointment">
  <div class="appointment-photo" role="img" aria-label="Woman with long wavy hair touching her hair, black and white"></div>
  <div class="appointment-card">
    <h2 class="script">Make an Appointment</h2>
    <p>Booking online takes less than a minute. Choose your service, pick a time that suits you and we will confirm by email. Sign up today to receive seasonal offers and studio news.</p>
    <a class="btn">Signup Now</a>
  </div>
</section>

<section class="services">
  <h2 class="section-title script">Our Services</h2>
  <p class="section-intro">From soothing facials to smooth waxing and lasting skincare plans, our menu is built around you. Browse the treatments below and book the one that fits your day.</p>
  <div class="service-grid">
    <div class="service-card"><div class="photo" role="img" aria-label="Client relaxing during a facial treatment"></div><div class="label">Facials Services</div></div>
    <div class="service-card"><div class="photo" role="img" aria-label="Client receiving a waxing treatment"></div><div class="label">Waxing Services</div></div>
    <div class="service-card"><div class="photo" role="img" aria-label="Client receiving a skincare treatment"></div><div class="label">Skincare Services</div></div>
  </div>
</section>

<section class="prices">
  <h2 class="section-title script">Our Prices</h2>
  <p class="section-intro">Clear prices, no surprises. Every treatment includes a short consultation.</p>
  <div class="price-grid">
    <div class="price-item"><div class="head"><span>Facials</span><span>$ 80</span></div><p>A deep cleanse, gentle exfoliation and hydrating mask matched to your skin type, finished with a calming massage and light moisturiser.</p></div>
    <div class="price-item"><div class="head"><span>Waxing</span><span>$ 45</span></div><p>Quick, careful waxing for brows, lip, legs and more using warm low-temperature wax that is kind to sensitive skin.</p></div>
    <div class="price-item"><div class="head"><span>Skincare</span><span>$ 90</span></div><p>A personal plan built over several visits, with peels, serums and home care advice to keep your skin clear and bright.</p></div>
    <div class="price-item"><div class="head"><span>Hair Removal</span><span>$ 27</span></div><p>Long-lasting smooth results for face and body, done by licensed staff in a private, relaxing room.</p></div>
  </div>
</section>

<section class="gallery">
  <svg class="band" width="1200" height="300" viewBox="0 0 1200 300" aria-hidden="true">
    <path d="M0 30Q600 -10 1200 30V300H0Z" fill="#000000"/>
  </svg>
  <h2 class="section-title script">Gallery</h2>
  <svg class="arrow prev" width="16" height="24" viewBox="0 0 16 24" aria-hidden="true"><path d="M13 2L3 12L13 22" fill="none" stroke="#ffffff" stroke-width="3"/></svg>
  <div class="gallery-row">
    <div class="photo" role="img" aria-label="Spa treatment with hands and towels"></div>
    <div class="photo" role="img" aria-label="Salon products and tools"></div>
    <div class="photo" role="img" aria-label="Client during a beauty treatment"></div>
    <div class="photo" role="img" aria-label="Styled updo hairstyle"></div>
  </div>
  <svg class="arrow next" width="16" height="24" viewBox="0 0 16 24" aria-hidden="true"><path d="M3 2L13 12L3 22" fill="none" stroke="#ffffff" stroke-width="3"/></svg>
</section>

<footer class="site-footer">
  <div class="footer-col col-info"><h3>Information</h3><a>Home</a><a>Services</a><a>Pricing</a><a>Gallery</a></div>
  <div class="footer-col col-links"><h3>Quick Links</h3><a>Sign Up</a><a>Appointment Booking</a><a>Contact Us</a><a>Privacy Policy</a></div>
  <div class="footer-col col-more"><h3>&nbsp;</h3><a>Mail Us</a><a>Newsletter Signup</a><a>News</a><a>Sitemap</a></div>
  <div class="contact-box">
    <div class="contact-row">
      <span class="icon-circle"><svg width="18" height="18" viewBox="0 0 24 24" aria-hidden="true"><path d="M6.6 10.8a15 15 0 0 0 6.6 6.6l2.2-2.2a1 1 0 0 1 1-.25 11.4 11.4 0 0 0 3.6.57 1 1 0 0 1 1 1V20a1 1 0 0 1-1 1A17 17 0 0 1 3 4a1 1 0 0 1 1-1h3.5a1 1 0 0 1 1 1c0 1.25.2 2.45.57 3.6a1 1 0 0 1-.25 1z" fill="#ffffff"/></svg></span>
      <span>123 456 780 (0000)</span>
    </div>
    <div class="social"><span></span><span></span><span></span><span></span><span></span></div>
    <div class="contact-row email">
      <span class="icon-circle"><svg width="18" height="14" viewBox="0 0 18 14" aria-hidden="true"><rect x="1" y="1" width="16" height="12" fill="none" stroke="#ffffff" stroke-width="1.6"/><path d="M1 1L9 8L17 1" fill="none" stroke="#ffffff" stroke-width="1.6"/></svg></span>
      <span>info@dozing-heron.com</span>
    </div>
  </div>
  <p class="copyright">Copyright © 2024 Dozing Heron. All Rights Reserved.</p>
</footer>

</body>
</html>
```